Town of Merrowfield Commercial Development

Create introduction point with 3 subheading categories. The bullets under the 3 categories should be where to use the infographics. Keep the Town of Merrowfield logo in the piece. The layout can be vertical or horizontal. Would like to stay on one page.

Target Market(s)

Commercial real estate developers and corporations

Industry/Entity Type

Real estate

Font styles to use
Serif

Requirements
Must have
• Business to business looking
Should not have
• Not comical

```html
<!DOCTYPE html>
<html lang="en">
<head>
<meta charset="utf-8">
<title>Town of Merrowfield – Commercial Development</title>
<link rel="stylesheet" href="https://fonts.googleapis.com/css2?family=Montserrat:wght@600;700;800&family=Poppins:wght@400;600;700&family=Libre+Baskerville:wght@400&display=swap">
<style>
  :root {
    --teal: #1f6e78;
    --red: #9c252b;
    --charcoal: #3a3d40;
    --ink: #2b2b2b;
    --paper: #ffffff;
    --stage: #eeeeee;
  }
  * { box-sizing: border-box; margin: 0; padding: 0; }
  html, body { width: 671px; height: 1200px; overflow: hidden; background: var(--stage); }
  .flyer {
    position: absolute; left: 20px; top: 377px;
    width: 631px; height: 445px;
    background: var(--paper);
    box-shadow: 0 4px 14px rgba(0,0,0,.18);
    overflow: hidden;
    font-family: "Poppins", sans-serif;
    color: var(--ink);
  }
  .header-art { position: absolute; left: 0; top: 0; width: 631px; height: 99px; }
  .brand { position: absolute; left: 22px; top: 26px; width: 96px; text-align: center; }
  .brand-dot { width: 34px; height: 34px; border-radius: 50%; background: var(--red); margin: 0 auto 6px; }
  .brand-name {
    font-family: "Libre Baskerville", serif; font-weight: 400;
    font-size: 13px; line-height: 1.1; color: var(--ink);
  }
  .intro { position: absolute; left: 157px; top: 22px; width: 466px; color: var(--paper); }
  .intro-title {
    font-family: "Montserrat", sans-serif; font-weight: 700; font-size: 17.5px;
    line-height: 1.15; white-space: nowrap;
  }
  .intro-text { font-family: "Montserrat", sans-serif; font-weight: 700; font-size: 10.2px; line-height: 1.27; margin-top: 5px; }
  .pillar {
    position: absolute; top: 150px; width: 174px; height: 243px;
    border: 1.5px solid var(--accent); border-top: none;
    border-radius: 10px 10px 12px 12px;
    border-bottom-width: 4px;
    background: var(--paper);
  }
  .pillar--location { left: 42px; --accent: var(--red); }
  .pillar--community { left: 228px; --accent: var(--teal); }
  .pillar--business { left: 413px; --accent: var(--red); }
  .pillar-head {
    height: 49px; background: var(--accent); border-radius: 10px 10px 0 0;
    color: var(--paper); font-family: "Montserrat", sans-serif; font-weight: 700;
    font-size: 18.5px; text-align: center; padding-top: 20px; margin: 0 -1.5px;
  }
  .pillar-icon {
    position: absolute; left: 50%; top: -45px; margin-left: -28px;
    width: 56px; height: 56px; border-radius: 50%;
    background: var(--charcoal); border: 3px solid var(--paper);
    display: flex; align-items: center; justify-content: center;
  }
  .facts { list-style: none; padding: 13px 6px 0 9px; }
  .fact {
    position: relative; padding-left: 11px; margin-bottom: 8px;
    font-size: 7.6px; line-height: 1.18;
  }
  .fact svg { position: absolute; left: 0; top: 1px; width: 7px; height: 7px; color: var(--red); }
  .hl { color: var(--accent); }
  .hl-b { color: var(--accent); font-weight: 600; }
  .web {
    position: absolute; left: 0; right: 0; top: 410px; text-align: center;
    font-family: "Poppins", sans-serif; font-size: 14.5px; letter-spacing: 2px; color: var(--ink);
  }
  .web span { color: var(--red); }
</style>
</head>
<body>
<svg width="0" height="0" style="position:absolute">
  <defs>
    <symbol id="tick" viewBox="0 0 10 10">
      <circle cx="5" cy="5" r="4.2" fill="none" stroke="currentColor" stroke-width="1"/>
      <path d="M3 5.1 L4.5 6.5 L7.2 3.6" fill="none" stroke="currentColor" stroke-width="1.1"/>
    </symbol>
  </defs>
</svg>

<main class="flyer">
  <svg class="header-art" viewBox="0 0 631 99" aria-hidden="true">
    <rect x="0" y="0" width="631" height="10" fill="var(--teal)"/>
    <polygon points="125,0 631,0 631,99 153,99" fill="var(--teal)"/>
    <polygon points="114,10 118,10 147,99 143,99" fill="var(--red)"/>
  </svg>

  <div class="brand">
    <div class="brand-dot"></div>
    <div class="brand-name">Town of Merrowfield</div>
  </div>

  <header class="intro">
    <h1 class="intro-title">LOCATING YOUR BUSINESS TO MERROWFIELD</h1>
    <p class="intro-text">could be the smartest move your company ever makes. Our location, employment base, smart growth and college town charm make it a stand-out from other communities.</p>
  </header>

  <section class="pillar pillar--location">
    <div class="pillar-icon">
      <svg width="26" height="28" viewBox="0 0 26 28"><path d="M13 2a8 8 0 0 0-8 8c0 6 8 13 8 13s8-7 8-13a8 8 0 0 0-8-8z" fill="#fff"/><circle cx="13" cy="10" r="3" fill="var(--charcoal)"/><path d="M4 22 L13 27 L22 22" fill="none" stroke="#fff" stroke-width="2"/></svg>
    </div>
    <h2 class="pillar-head">LOCATION</h2>
    <ul class="facts">
      <li class="fact"><svg><use href="#tick"/></svg>Merrowfield is just <b class="hl-b">20 miles</b> north of Ashford, NC in Greyling County</li>
      <li class="fact"><svg><use href="#tick"/></svg>Conveniently located off <b class="hl-b">I-77 and 73</b></li>
      <li class="fact"><svg><use href="#tick"/></svg>Within a day’s <b class="hl-b">drive of 40%</b> of the U.S. population, making business close to suppliers and customers alike</li>
      <li class="fact"><svg><use href="#tick"/></svg><b class="hl-b">30 minutes</b> from Ashford Regional International Airport</li>
      <li class="fact"><svg><use href="#tick"/></svg>Located in the <b class="hl-b">Ashford MSA</b></li>
      <li class="fact"><svg><use href="#tick"/></svg>Home of <b class="hl-b">Merrowfield College</b></li>
      <li class="fact"><svg><use href="#tick"/></svg>Three hours to beautiful beaches, two hours to <b class="hl-b">scenic mountains</b></li>
    </ul>
  </section>

  <section class="pillar pillar--community">
    <div class="pillar-icon">
      <svg width="30" height="24" viewBox="0 0 30 24" fill="#fff"><circle cx="15" cy="6" r="4.5"/><circle cx="6" cy="8" r="3.3"/><circle cx="24" cy="8" r="3.3"/><path d="M7 22c0-5 3.5-8 8-8s8 3 8 8z"/><path d="M0 20c0-4 2.5-6.5 6-6.5 1 0 2 .2 2.6.6C7 16 6 18 6 20z"/><path d="M30 20c0-4-2.5-6.5-6-6.5-1 0-2 .2-2.6.6 1.6 1.9 2.6 3.9 2.6 5.9z"/></svg>
    </div>
    <h2 class="pillar-head">COMMUNITY</h2>
    <ul class="facts">
      <li class="fact"><svg><use href="#tick"/></svg>Merrowfield is one of the fastest growing affluent populations in North Carolina with a median income of <b class="hl-b">$131,144 and population of 15,132</b></li>
      <li class="fact"><svg><use href="#tick"/></svg>More than <b class="hl-b">74% of Merrowfield’s</b> <span class="hl">residents</span> over the age of 25 hold a bachelor’s degree or higher</li>
      <li class="fact"><svg><use href="#tick"/></svg>In national citizen surveys, Merrowfield <b class="hl-b">ranks #1 in “sense of community”</b></li>
      <li class="fact"><svg><use href="#tick"/></svg><b class="hl-b">Merrowfield’s lake amenities, parks, greenways, first-rate schools, low crime rate and proximity</b> to Merrowfield College make it a great place to live and work.</li>
    </ul>
  </section>

  <section class="pillar pillar--business">
    <div class="pillar-icon">
      <svg width="28" height="24" viewBox="0 0 28 24"><rect x="9" y="1.5" width="10" height="5" rx="1.5" fill="none" stroke="#fff" stroke-width="2"/><rect x="1" y="6" width="26" height="17" rx="2" fill="#fff"/><rect x="1" y="12" width="26" height="1.5" fill="var(--charcoal)"/><rect x="12" y="10.5" width="4" height="4.5" fill="var(--charcoal)"/></svg>
    </div>
    <h2 class="pillar-head">BUSINESS</h2>
    <ul class="facts">
      <li class="fact"><svg><use href="#tick"/></svg>Merrowfield’s major employers include <b class="hl-b">Halvorsen Climate Systems, Keystone Industrial Supply, Brightline Tool Works, and Merrowfield College.</b></li>
      <li class="fact"><svg><use href="#tick"/></svg>Merrowfield has a thriving Farmer’s Market and is home to <b class="hl-b">over 30 restaurants including</b> Golden Ladle Award nominees.</li>
      <li class="fact"><svg><use href="#tick"/></svg>Merrowfield promotes a culture of supporting local independent businesses through our <b class="hl-b">active business retention program, various funding programs, and small business networking opportunities.</b></li>
    </ul>
  </section>

  <p class="web">www.<span>townofmerrowfield</span>.org</p>
</main>
</body>
</html>
```